Webdesign für für einen Kaufwerk 5 Shop für eine Outdoormarke
Zielgruppe
Wir verkaufen Bergschuhe und Badehosen unter der Marke Bralvo Ridge. Hauptsächlich handelt es sich um Outdoorprodukte.
Aufgabenstellung
Wir möchten einen Bralvo Ridge Outdoor und Bademoden Shop aufbauen. Das Template sollte auf Kaufwerk 5 aufgebaut sein.
Die webseite sollte Modern sein und viele Bildelemente enthalten. (Bilder sind vorhanden)
Wir möchten ein Design das man für den Outdoorbereich und für den Bademodenbreich verwenden kann.
Im Fokus soll die Seite unser Unternehmen bzw. Marke präsentieren. Im zweiten Schritt möchten wir unsere Ware dort verkaufen.
https://www.tesvarin.ch/

```html
<!DOCTYPE html>
<html lang="de">
<head>
<meta charset="utf-8">
<title>Bralvo Ridge – Shop Entwurf</title>
<link href="https://fonts.googleapis.com/css2?family=Montserrat:wght@400;500;600;700&display=swap" rel="stylesheet">
<style>
  :root{
    --ink:#1d1d1d;
    --white:#ffffff;
    --paper:#ffffff;
    --panel:#f2f2f2;
    --line:#e2e2e2;
    --accent:#1c7fb6;
    --sky:#7fb2cf;
    --rock:#5c4f63;
    --earth:#8a6a52;
    --lake:#5a8aa6;
  }
  html,body{margin:0;padding:0;width:907px;height:1200px;overflow:hidden;background:var(--paper);}
  body{font-family:'Montserrat',sans-serif;color:var(--ink);}
  .stage{position:absolute;left:0;top:0;width:1240px;height:1640px;transform:scale(0.7315);transform-origin:0 0;}
  .screen{position:absolute;width:998px;height:783px;overflow:hidden;background:var(--white);box-shadow:0 2px 10px rgba(0,0,0,.18);}
  .screen--home{left:175px;top:17px;}
  .screen--category{left:214px;top:832px;width:1002px;}
  .hero{position:absolute;left:0;top:138px;width:100%;height:600px;}
  .hero--lake{background:linear-gradient(180deg,#86b8d3 0%,#a9c4d3 14%,#6f6680 30%,#7a5e55 48%,#8c6b4f 62%,#5f86a3 72%,#4f7f9e 100%);}
  .hero--valley{background:linear-gradient(180deg,#a3a8c2 0%,#6d6a8a 18%,#6e5a5c 34%,#7a5f4e 50%,#5a4c5c 62%,#7a6a55 70%,#5f90ab 74%,#4d7f9c 100%);}
  .strip{position:absolute;left:0;top:738px;width:100%;height:45px;}
  .strip--home{background:linear-gradient(90deg,#3c6b2e 0%,#5f8c3a 12%,#c98e62 18%,#d59c6e 60%,#c78a5a 80%,#7fae52 90%,#9cc46a 100%);}
  .strip--category{background:linear-gradient(90deg,#6e7a4a 0%,#8a6a4a 20%,#5e4a3a 34%,#6e9a4a 36%,#8fb56a 60%,#e0b08a 66%,#eadbe2 80%,#e9dde6 100%);}
  .close{position:absolute;left:28px;top:80px;width:22px;height:22px;}
  .brand{position:absolute;display:flex;align-items:center;gap:10px;font-weight:700;font-size:26px;letter-spacing:1px;white-space:nowrap;color:var(--ink);}
  .brand__dot{width:22px;height:22px;border-radius:50%;background:var(--ink);flex:none;}
  .screen--home .brand{left:850px;top:40px;}
  .screen--category .brand{left:4px;top:24px;}
  .mainnav{position:absolute;display:flex;gap:30px;font-size:12.5px;font-weight:500;white-space:nowrap;}
  .screen--home .mainnav{left:747px;top:118px;}
  .screen--category .mainnav{right:796px;top:118px;}
  .hero-title{position:absolute;color:var(--white);font-weight:600;font-size:35px;letter-spacing:2.5px;white-space:nowrap;}
  .hero-rule{position:absolute;height:4px;background:var(--accent);}
  .offcanvas{position:absolute;left:6px;top:138px;width:339px;height:418px;background:var(--white);}
  .offcanvas__tools{display:flex;height:60px;border-bottom:1px dashed var(--line);align-items:center;}
  .tool{flex:1;display:flex;flex-direction:column;align-items:center;justify-content:center;font-size:8px;}
  .tool svg{width:20px;height:20px;}
  .search{display:flex;justify-content:space-between;align-items:center;height:58px;padding:0 10px;border-bottom:1px solid var(--line);font-size:11.5px;}
  .menu{list-style:none;margin:0;padding:16px 10px 0;font-size:11.5px;}
  .menu li{height:27.3px;line-height:18px;}
  .menu li.is-active{font-weight:700;}
  .filter-toggle{position:absolute;left:861px;top:113px;display:flex;align-items:center;gap:8px;font-weight:700;font-size:11.5px;}
  .filters{position:absolute;left:669px;top:138px;width:315px;height:418px;background:var(--panel);}
  .filters__tabs{position:absolute;left:46px;top:36px;display:flex;gap:28px;font-size:11.5px;white-space:nowrap;}
  .filters__tabs .is-active{font-weight:700;}
  .instock{position:absolute;left:45px;top:75px;width:238px;display:flex;align-items:center;gap:8px;font-size:11.5px;}
  .instock__box{width:11px;height:11px;border:1px solid #ddd;background:var(--white);}
  .instock svg{margin-left:auto;}
  .facets{position:absolute;left:34px;top:102px;width:259px;list-style:none;margin:0;padding:0;}
  .facet{height:32px;border:1px solid var(--line);background:var(--white);margin-bottom:5px;display:flex;align-items:center;justify-content:space-between;padding:0 10px 0 11px;font-size:11.5px;}
</style>
</head>
<body>
<div class="stage">

  <section class="screen screen--home">
    <svg class="close" viewBox="0 0 22 22"><path d="M2 2L20 20M20 2L2 20" stroke="#1d1d1d" stroke-width="2"/></svg>
    <div class="brand"><span class="brand__dot"></span>BRALVO RIDGE</div>
    <nav class="mainnav"><span>HOME</span><span>SWIM SUITS</span><span>TREKKING SHOES</span></nav>
    <div class="hero hero--lake" role="img" aria-label="Berglandschaft mit Wasserfall und See"></div>
    <div class="strip strip--home" role="img" aria-label="Produktfoto im Grünen"></div>
    <div class="hero-title" style="left:635px;top:381px;">SWIM SUITS</div>
    <div class="hero-title" style="left:970px;top:381px;">TREKKING SHOES</div>
    <div class="hero-rule" style="left:972px;top:437px;width:340px;"></div>

    <aside class="offcanvas">
      <div class="offcanvas__tools">
        <div class="tool"><svg viewBox="0 0 20 20"><path d="M10 3V17M3 10H17" stroke="#1d1d1d" stroke-width="2"/></svg></div>
        <div class="tool"><svg viewBox="0 0 20 20"><path d="M10 17L3 10A4 4 0 0 1 10 5A4 4 0 0 1 17 10Z" fill="#1d1d1d"/></svg></div>
        <div class="tool"><svg viewBox="0 0 20 20"><circle cx="10" cy="6" r="4" fill="#1d1d1d"/><path d="M2 19C2 13 6 11 10 11S18 13 18 19Z" fill="#1d1d1d"/></svg></div>
        <div class="tool"><svg viewBox="0 0 20 20"><path d="M1 3H4L6 13H16L18 6H5" fill="#1d1d1d" stroke="#1d1d1d" stroke-width="1.5"/><circle cx="7" cy="17" r="1.6" fill="#1d1d1d"/><circle cx="15" cy="17" r="1.6" fill="#1d1d1d"/></svg><span>0,00 €</span></div>
      </div>
      <div class="search"><span>SUCHBEGRIFF</span><svg width="22" height="22" viewBox="0 0 22 22"><circle cx="9" cy="9" r="6.5" fill="none" stroke="#1d1d1d" stroke-width="2.6"/><path d="M14 14L20 20" stroke="#1d1d1d" stroke-width="3"/></svg></div>
      <ul class="menu">
        <li class="is-active">HOME</li><li>LOGIN / REGISTRIEREN</li><li>ÜBER BRALVO RIDGE</li><li>SWIM SUITS</li><li>TREKKING SHOES</li><li>BLOG</li><li>CONTACT</li><li>AGB</li><li>VERSAND</li><li>IMPRESSUM</li>
      </ul>
    </aside>
  </section>

  <section class="screen screen--category">
    <div class="brand"><span class="brand__dot"></span>BRALVO RIDGE</div>
    <nav class="mainnav"><span>TREKKING SHOES</span><span>BLOG</span><span>CONTACT</span></nav>
    <div class="filter-toggle"><svg width="16" height="16" viewBox="0 0 16 16"><path d="M0 1H16L10 8V15L6 13V8Z" fill="#1d1d1d"/></svg>FILTERN</div>
    <div class="hero hero--valley" role="img" aria-label="Bergtal mit Nebel und See"></div>
    <div class="strip strip--category" role="img" aria-label="Produktfotos Schuhe und Bademode"></div>
    <div class="hero-title" style="left:0;top:380px;">TREKKING SHOES</div>
    <div class="hero-rule" style="left:0;top:436px;width:335px;"></div>

    <aside class="filters">
      <div class="filters__tabs"><span>SWIM SUITS</span><span>|</span><span class="is-active">TREKKING SHOES</span></div>
      <div class="instock"><span class="instock__box"></span>SOFORT LIEFERBAR
        <svg width="13" height="13" viewBox="0 0 13 13"><path d="M2 6A4.5 4.5 0 0 1 10 3.5M11 7A4.5 4.5 0 0 1 3 9.5" fill="none" stroke="#999" stroke-width="1.2"/><path d="M10 1V4H7M3 12V9H6" fill="none" stroke="#999" stroke-width="1.2"/></svg>
      </div>
      <ul class="facets">
        <li class="facet">ARTIKELTYP<svg width="14" height="9" viewBox="0 0 14 9"><path d="M1 1L7 7L13 1" fill="none" stroke="#1d1d1d" stroke-width="2.2"/></svg></li>
        <li class="facet">GRÖSSE<svg width="14" height="9" viewBox="0 0 14 9"><path d="M1 1L7 7L13 1" fill="none" stroke="#1d1d1d" stroke-width="2.2"/></svg></li>
        <li class="facet">DAMEN<svg width="14" height="9" viewBox="0 0 14 9"><path d="M1 1L7 7L13 1" fill="none" stroke="#1d1d1d" stroke-width="2.2"/></svg></li>
        <li class="facet">HERREN<svg width="14" height="9" viewBox="0 0 14 9"><path d="M1 1L7 7L13 1" fill="none" stroke="#1d1d1d" stroke-width="2.2"/></svg></li>
        <li class="facet">FARBE<svg width="14" height="9" viewBox="0 0 14 9"><path d="M1 1L7 7L13 1" fill="none" stroke="#1d1d1d" stroke-width="2.2"/></svg></li>
        <li class="facet">MATERIAL<svg width="14" height="9" viewBox="0 0 14 9"><path d="M1 1L7 7L13 1" fill="none" stroke="#1d1d1d" stroke-width="2.2"/></svg></li>
        <li class="facet">BEWERTUNGEN<svg width="14" height="9" viewBox="0 0 14 9"><path d="M1 1L7 7L13 1" fill="none" stroke="#1d1d1d" stroke-width="2.2"/></svg></li>
      </ul>
    </aside>
  </section>

</div>
</body>
</html>
```